P&H RESTORATION

I want a brochure similiar to the example i've attached.
My company name is P&H Restoration. The website is: P-H-Restoration.com.
The phone number is 803.417.9056.

I don't like the "yellow" being the main color of the example so I'm open to suggestions. I want something CLEAN & Simple, like our logo . This will be a bi fold brochure

```html
<!DOCTYPE html>
<html lang="en">
<head>
<meta charset="utf-8">
<title>P&amp;H Restoration — Bi-fold Brochure</title>
<link rel="stylesheet" href="https://fonts.googleapis.com/css2?family=Josefin+Sans:wght@300;400;600&family=Great+Vibes&display=swap">
<style>
  :root {
    --stage: #4a4a4a;
    --ink: #111111;
    --paper: #ffffff;
    --paper-soft: #f1f1f1;
    --muted: #cfcfcf;
    --label: #f4f4f4;
    --sans: "Josefin Sans", "Helvetica Neue", Arial, sans-serif;
    --script: "Great Vibes", cursive;
  }
  * { box-sizing: border-box; margin: 0; padding: 0; }
  html, body { width: 900px; height: 1200px; overflow: hidden; }
  body { background: var(--stage); font-family: var(--sans); color: var(--ink); position: relative; }

  .spread { position: absolute; left: 80px; width: 740px; height: 520px; background: var(--paper); overflow: hidden; box-shadow: 0 6px 18px rgba(0,0,0,.35); }
  .spread--front { top: 40px; }
  .spread--back { top: 635px; }
  .side-label { position: absolute; left: 0; width: 900px; text-align: center; color: var(--label); font-size: 18px; letter-spacing: 2px; font-weight: 300; }
  .side-label--front { top: 572px; }
  .side-label--back { top: 1167px; }

  .abs { position: absolute; }
  .black-field { background: var(--ink); }
  .white-bar { background: linear-gradient(90deg, var(--paper), var(--paper-soft)); }
  .white-foot { background: linear-gradient(180deg, var(--paper-soft), var(--paper)); }

  .brand-name { position: absolute; display: flex; align-items: center; gap: 6px; background: var(--paper); padding: 6px 10px; font-family: var(--sans); font-weight: 400; font-size: 13px; letter-spacing: 1px; color: var(--ink); white-space: nowrap; }
  .brand-name .brand-square { width: 8px; height: 8px; background: var(--ink); }

  .photo-frame { position: absolute; border: 2px solid var(--paper); }
  .photo { position: absolute; }
  .photo--plans { background: linear-gradient(135deg, #f4f4f4, #b9b9b9 70%, #8c8c8c); }
  .photo--damaged-room { background: linear-gradient(160deg, #efe6d2 0%, #c9ab7a 50%, #7a5a34 100%); }
  .photo--flooded-kitchen { background: linear-gradient(180deg, #d9dde2 0%, #8a9099 45%, #233245 75%, #0f1a28 100%); }
  .photo--vent { background: linear-gradient(135deg, #6c665d, #2b2824); }
  .photo--duct { background: linear-gradient(135deg, #c9c4bc, #5e5a55); }
  .photo--drain { background: linear-gradient(135deg, #8a6a4a, #2e2117); }
  .photo--mold { background: linear-gradient(135deg, #a79e8a, #4c4538); }

  .tagline-script { font-family: var(--script); color: var(--paper); font-size: 19px; }
  .phone { font-size: 15px; letter-spacing: 3px; font-weight: 400; }
  .small-line { font-size: 9.5px; letter-spacing: 1.5px; font-weight: 300; }
  .headline-caps { font-size: 14px; letter-spacing: 1px; font-weight: 300; }
  .headline-script { font-family: var(--script); font-size: 30px; line-height: 1; }

  .stripes { position: absolute; display: flex; flex-direction: column; gap: 5px; }
  .stripes span { display: block; width: 28px; height: 6px; background: var(--ink); }

  .services { position: absolute; left: 552px; top: 66px; width: 176px; color: var(--paper); text-align: center; }
  .services-title { font-size: 15px; font-weight: 400; letter-spacing: 1px; margin-bottom: 10px; }
  .services-title em { font-family: var(--script); font-style: normal; font-size: 19px; letter-spacing: 0; }
  .service h3 { font-size: 9px; font-weight: 600; font-style: italic; margin-bottom: 4px; }
  .service p { font-size: 7px; line-height: 1.3; font-weight: 300; margin-bottom: 11px; }

  .offer { font-size: 10.5px; line-height: 1.3; font-weight: 400; }
</style>
</head>
<body>

<section class="spread spread--front" aria-label="Brochure front">
  <div class="abs black-field" style="left:0;top:0;width:740px;height:376px;"></div>
  <div class="abs white-bar" style="left:367px;top:0;width:373px;height:46px;"></div>
  <p class="abs tagline-script" style="left:55px;top:40px;">Serving the Greater Lakeview Area</p>
  <div class="photo photo--plans" role="img" aria-label="Photo of rolled architectural plans" style="left:0;top:92px;width:340px;height:184px;"></div>
  <div class="brand-name" style="left:568px;top:48px;"><span class="brand-square"></span>P&amp;H Restoration</div>
  <div class="photo-frame" style="left:388px;top:90px;width:352px;height:268px;"></div>
  <div class="photo photo--damaged-room" role="img" aria-label="Photo of a water damaged living room" style="left:400px;top:102px;width:340px;height:246px;"></div>

  <div class="abs white-foot" style="left:0;top:376px;width:740px;height:144px;"></div>
  <p class="abs phone" style="left:90px;top:422px;">803.417.9056</p>
  <p class="abs small-line" style="left:90px;top:447px;">office@P-H-Restoration.com</p>
  <p class="abs small-line" style="left:90px;top:470px;">www.P-H-Restoration.com</p>
  <div class="stripes" style="left:0;top:455px;"><span></span><span></span><span></span></div>
  <div class="abs black-field" style="left:285px;top:496px;width:165px;height:24px;"></div>
  <p class="abs headline-caps" style="left:470px;top:398px;">THREE GENERATIONS OF</p>
  <p class="abs headline-script" style="left:470px;top:420px;">Restoration Experience</p>
  <p class="abs small-line" style="left:505px;top:470px;">www.P-H-Restoration.com</p>
</section>
<p class="side-label side-label--front">FRONT</p>

<section class="spread spread--back" aria-label="Brochure inside">
  <div class="abs black-field" style="left:0;top:0;width:740px;height:440px;"></div>
  <div class="abs white-bar" style="left:0;top:0;width:367px;height:37px;"></div>

  <div class="photo photo--vent" role="img" aria-label="Photo of a dirty vent" style="left:28px;top:64px;width:100px;height:76px;border:2px solid var(--paper);"></div>
  <div class="photo photo--duct" role="img" aria-label="Photo of duct cleaning equipment" style="left:28px;top:156px;width:100px;height:76px;border:2px solid var(--paper);"></div>
  <div class="photo photo--drain" role="img" aria-label="Photo of a damaged floor drain" style="left:28px;top:248px;width:100px;height:76px;border:2px solid var(--paper);"></div>
  <div class="photo photo--mold" role="img" aria-label="Photo of mold on a wall" style="left:28px;top:340px;width:100px;height:76px;border:2px solid var(--paper);"></div>

  <div class="photo-frame" style="left:150px;top:92px;width:382px;height:322px;"></div>
  <div class="photo photo--flooded-kitchen" role="img" aria-label="Photo of a flooded modern kitchen" style="left:162px;top:104px;width:358px;height:298px;"></div>

  <div class="brand-name" style="left:570px;top:10px;"><span class="brand-square"></span>P&amp;H Restoration</div>

  <div class="services">
    <h2 class="services-title">OUR <em>Services</em></h2>
    <div class="service">
      <h3>Duct Cleaning</h3>
      <p>Keep the air in your home clean. Cleaning your air ducts can help ease allergies, asthma and other illnesses linked to poor air quality and keeps your family safe and healthy.</p>
    </div>
    <div class="service">
      <h3>Dryer Vent Cleaning</h3>
      <p>A clogged dryer vent can cost you loads of money through high electric bills and dryer overheating. Lint that forms inside the vent is harmful to your home. We recommend cleaning your dryer vent every two to three years.</p>
    </div>
    <div class="service">
      <h3>Water Damage Restoration</h3>
      <p>Broken pipes, leaks or a recent flood? Should your home face water damage, big or small, call P&amp;H Restoration right away to limit the damage to your property and the cost of repair.</p>
    </div>
    <div class="service">
      <h3>Mold Remediation</h3>
      <p>Mold can develop in almost any home or office in a very small amount of time and moisture. Mold can spread within a house within 48-72 hours of developing. This can lead to health risks for everyone in the house.</p>
    </div>
  </div>

  <div class="abs white-foot" style="left:0;top:440px;width:740px;height:80px;"></div>
  <p class="abs offer" style="left:40px;top:452px;width:360px;">We are now offering Dryer Vent Cleaning. Don't waste energy by over running a dryer with a clogged vent or worse start a house fire with a clogged vent!</p>
  <p class="abs phone" style="left:470px;top:448px;font-size:16px;">803.417.9056</p>
  <p class="abs small-line" style="left:470px;top:473px;">www.P-H-Restoration.com</p>
</section>
<p class="side-label side-label--back">BACK</p>

</body>
</html>
```